Website for keystone mobile detailing.

Need a homepage, pages for: car and truck detailing, boat detailing, airplane detailing, about us, contact us. I have the domain name through nimbuspark so I will need the design uploaded on my domain. Also hoping to link other domains to this page.I would like to see the logo more pronounced. I would like to see a large phone number link to call my business. The layout looks nice but the pics need to depict car washing and waxing not car mechanics. i would like the colors of the webpage to incorporate the colors found in the logo in some way. I would like links to social media pages

Target Market(s)

Local customers in Vero Beach, Florida.

Number of Pages Required

5+ page

Colors

Designer to choose colors to be used in the design.

Requirements
Must have
• Easy to navigate, attractive pages with pictures and logo, professional looking. must have my phone number and logo very prevalent and links to call or go to home page. I would like links to my social media accounts on the home page.
Nice to have
• Easy to navigate, attractive pages with pictures and logo, professional looking.

```html
<!DOCTYPE html>
<html lang="en">
<head>
<meta charset="utf-8">
<title>Keystone Mobile Detailing</title>
<link href="https://fonts.googleapis.com/css2?family=Dosis:wght@400;500;600;700&display=swap" rel="stylesheet">
<style>
:root{
  --accent:#f04e23;
  --navy:#2d3a7a;
  --ink:#2b2b2b;
  --muted:#555;
  --line:#dcdcdc;
  --footer:#151b2c;
  --white:#fff;
}
*{box-sizing:border-box;margin:0;padding:0}
html,body{width:1200px;height:2628px;overflow:hidden;background:var(--white)}
body{position:relative;font-family:'Dosis',sans-serif;color:var(--ink)}
a{color:inherit;text-decoration:none}
.btn{position:absolute;background:var(--accent);color:var(--white);font-weight:600;font-size:13px;letter-spacing:.5px;text-align:center;text-transform:uppercase}

/* header */
.site-header{position:absolute;left:0;top:0;width:1200px;height:78px;background:var(--white);box-shadow:0 1px 3px rgba(0,0,0,.08);z-index:2}
.brand{position:absolute;left:102px;top:16px;display:flex;align-items:center;gap:10px}
.brand-mark{width:36px;height:36px;border-radius:50%;background:var(--navy)}
.brand-name{display:block;font-size:24px;font-weight:700;color:var(--navy);line-height:1}
.brand-phone{display:block;font-size:13px;font-weight:700;color:var(--navy);letter-spacing:1px;margin-top:3px}
.main-nav{position:absolute;right:86px;top:31px;display:flex;gap:28px;font-size:13px;color:var(--navy);text-transform:uppercase}
.main-nav a.active{border-bottom:2px solid var(--accent);padding-bottom:5px}

/* hero */
.hero{position:absolute;left:0;top:78px;width:1200px;height:474px;background:linear-gradient(100deg,#e8e6e2 0%,#d6d9dc 45%,#c9ccd0 70%,#e4e2dc 100%)}
.hero-call{position:absolute;left:86px;top:150px;font-size:36px;font-weight:700;color:#222;letter-spacing:1px}
.hero-call a{color:var(--accent)}
.hero-text{position:absolute;left:86px;top:200px;width:560px;font-size:18px;font-weight:500;line-height:27px;color:#222}
.hero .btn{left:86px;top:275px;width:140px;height:38px;line-height:38px}
.dots{position:absolute;left:1100px;top:186px}
.dots span{display:block;width:13px;height:13px;border-radius:50%;background:#b5b5b5;margin-bottom:12px}
.dots span.on{border:2px solid var(--accent);box-shadow:inset 0 0 0 2px var(--white);background:var(--accent)}

/* section titles */
.section-title{position:absolute;left:0;width:1200px;text-align:center;font-size:34px;font-weight:500;color:#333;letter-spacing:.5px}
.section-title::after{content:"";display:block;width:160px;height:1px;background:var(--accent);margin:6px auto 0}

/* services */
.service{position:absolute;top:672px;width:260px}
.service svg{position:absolute;left:0;top:0}
.service h3{margin-left:60px;font-size:13px;font-weight:700;color:#222;letter-spacing:.3px}
.service p{margin-left:60px;margin-top:10px;font-size:13px;line-height:21px;color:var(--muted)}

/* about */
.about{position:absolute;left:0;top:845px;width:1200px;height:453px;background:linear-gradient(90deg,#eef1f5,#f7f8fa 60%,#e1e7ef)}
.about-strip{position:absolute;left:0;top:0;width:350px;height:453px;background:linear-gradient(160deg,#1e2638,#3a465e)}
.about-photo{position:absolute;left:160px;top:56px;width:336px;height:336px;border-radius:50%;background:radial-gradient(circle at 55% 60%,#e9d36a 0,#6fa0b0 30%,#b9bcc2 60%,#8a8f98 100%);border:4px solid var(--white);box-shadow:0 0 0 2px #ccc}
.about h2{position:absolute;left:525px;top:92px;font-size:34px;font-weight:500;color:#222}
.about p{position:absolute;left:525px;top:148px;width:588px;font-size:13px;line-height:21px;color:#333}
.about .btn{left:525px;top:315px;width:138px;height:38px;line-height:38px}

/* testimonials */
.testimonial{position:absolute;left:257px;top:1440px;width:750px;height:158px;border:1px solid var(--line);background:var(--white)}
.avatar{position:absolute;left:207px;top:1460px;width:104px;height:104px;border-radius:50%;background:linear-gradient(#c9d6de,#9fb0bb);border:4px solid var(--white);box-shadow:0 0 0 1px var(--line)}
.testimonial p{position:absolute;left:72px;top:18px;width:652px;font-size:13px;line-height:21px;color:#333}
.byline{position:absolute;left:72px;top:118px;font-size:14px;color:#555}
.byline::before{content:"";display:inline-block;width:56px;height:1px;background:#bbb;vertical-align:middle;margin-right:10px}
.byline small{font-size:12px;color:#777}
.arrow{position:absolute;top:1583px;width:30px;height:30px;line-height:28px;text-align:center;font-size:18px}
.arrow.prev{left:910px;border:1px solid var(--line);color:var(--accent);background:var(--white)}
.arrow.next{left:946px;background:var(--accent);color:var(--white)}

/* blog */
.blog{position:absolute;left:0;top:1674px;width:1200px;height:546px;background:linear-gradient(180deg,#eef1f6,#e3e8f0 60%,#d8dee8);border-top:2px solid #e6e6e6}
.post{position:absolute;top:119px;width:501px;height:300px;background:var(--white);box-shadow:0 2px 6px rgba(0,0,0,.18)}
.post-photo{position:absolute;left:0;top:0;width:237px;height:300px;background:linear-gradient(135deg,#2b2f36,#6c727b 50%,#c98a5a 80%,#3a3d44)}
.post-meta{position:absolute;right:48px;top:0;width:212px;height:36px;background:var(--accent);color:var(--white);font-size:14px;line-height:36px;text-align:center;clip-path:polygon(8% 0,100% 0,92% 100%,0 100%)}
.post p{position:absolute;left:263px;top:74px;width:220px;font-size:13px;line-height:21px;color:#333}
.post .more{position:absolute;left:263px;top:244px;font-size:13px;color:#333;border-bottom:1px solid #333}
.blog .btn{left:531px;top:443px;width:138px;height:38px;line-height:38px}

/* footer */
.site-footer{position:absolute;left:0;top:2220px;width:1200px;height:360px;background:linear-gradient(160deg,#1a2033,#10141f)}
.site-footer h4{position:absolute;top:34px;font-size:16px;font-weight:600;color:var(--white);letter-spacing:.5px}
.field{position:absolute;left:86px;width:412px;background:var(--white);font-size:10px;color:#999;padding:7px 8px;text-transform:uppercase}
.site-footer .btn{left:86px;top:289px;width:131px;height:37px;line-height:37px}
.quick{position:absolute;left:612px;top:64px;list-style:none;font-size:13px;color:var(--white);text-transform:uppercase}
.quick li{height:42px}
.contacts{position:absolute;left:860px;top:64px;list-style:none;font-size:12px;color:var(--white);text-transform:uppercase}
.contacts li{height:42px}
.contacts .lower{text-transform:none}
.bottom-bar{position:absolute;left:0;top:2580px;width:1200px;height:48px;background:var(--accent)}
.social{position:absolute;left:86px;top:8px;display:flex;gap:13px}
.social a{width:34px;height:34px;border:1px solid rgba(255,255,255,.8)}
.copyright{position:absolute;right:86px;top:16px;font-size:12px;color:var(--white)}
</style>
</head>
<body>

<header class="site-header">
  <a class="brand" href="#">
    <span class="brand-mark"></span>
    <span>
      <span class="brand-name">Keystone Mobile Detailing</span>
      <span class="brand-phone">555-014-2280</span>
    </span>
  </a>
  <nav class="main-nav">
    <a class="active" href="#">Home</a>
    <a href="#">Car and Truck Detailing</a>
    <a href="#">Boat Detailing</a>
    <a href="#">Airplane Detailing</a>
    <a href="#">About Us</a>
    <a href="#">Contact Us</a>
  </nav>
</header>

<section class="hero" role="img" aria-label="Detailer polishing a car headlight with a buffer">
  <div class="hero-call">CALL US : <a href="tel:5550142280">555 - 014 - 2280</a></div>
  <p class="hero-text">Lorem Ipsum is simply dummy text of the printing and typesetting industry. Lorem Ipsum has been the industry's standard dummy textbook</p>
  <a class="btn" href="#">Read More</a>
  <div class="dots"><span></span><span></span><span class="on"></span></div>
</section>

<h2 class="section-title" style="top:602px">OUR SERVICES</h2>

<div class="service" style="left:86px">
  <svg width="38" height="26" viewBox="0 0 38 26" fill="none" stroke="#3a7bd5" stroke-width="1.6"><path d="M3 18V12l4-7h22l5 7v6z"/><path d="M7 12h25"/><circle cx="10" cy="19" r="3"/><circle cx="28" cy="19" r="3"/></svg>
  <h3>CAR AND TRUCK DETAILING</h3>
  <p>Lorem Ipsum is simply dummy text of the printing and typesetting industry. Lorem Ipsum has been the industry's standard dummy textbook .</p>
</div>
<div class="service" style="left:474px">
  <svg width="34" height="34" viewBox="0 0 34 34" fill="none" stroke="#3a7bd5" stroke-width="1.6"><path d="M17 3v18M17 5l8 10h-8"/><path d="M4 22h26l-4 7H8z"/></svg>
  <h3>BOAT DETAILING</h3>
  <p>Lorem Ipsum is simply dummy text of the printing and typesetting industry. Lorem Ipsum has been the industry's standard dummy textbook .</p>
</div>
<div class="service" style="left:863px">
  <svg width="34" height="34" viewBox="0 0 34 34" fill="none" stroke="#3a7bd5" stroke-width="1.6"><path d="M4 22l26-16-6 24-6-8-8 2z"/><path d="M18 22l12-16"/></svg>
  <h3>AIRPLANE DETAILING</h3>
  <p>Lorem Ipsum is simply dummy text of the printing and typesetting industry. Lorem Ipsum has been the industry's standard dummy textbook .</p>
</div>

<section class="about">
  <div class="about-strip" role="img" aria-label="Detailer working on a dark car"></div>
  <div class="about-photo" role="img" aria-label="Hand holding a polishing machine with a foam pad"></div>
  <h2>ABOUT US</h2>
  <p>Lorem Ipsum is simply dummy text of the printing and typesetting industry. Lorem Ipsum has been the industry's standard dummy text ever since the 1500s, when an unknown printer took a galley of type and scrambled it to make a type specimen book . Lorem Ipsum is simply dummy text of the printing and typesetting industry. Lorem Ipsum has been the industry's standard dummy text ever since the 1500s, when an unknown printer took a galley of type and scrambled it to make a type specimen book. It has survived not only five centuries, but also the leap into electronic typesetting, remaining essentially unchanged. It was popularised in the 1960s with the release of Typeline sheets</p>
  <a class="btn" href="#">Read More</a>
</section>

<h2 class="section-title" style="top:1350px">OUR SATISFIED CUSTOMERS</h2>
<div class="testimonial">
  <p>Lorem Ipsum is simply dummy text of the printing and typesetting industry. Lorem Ipsum has been the industry's standard dummy text ever since the 1500s, when an unknown printer took a galley of type and scrambled it to make a type specimen book . Lorem Ipsum is simply dummy text of the printing and typesetting industry. Lorem Ipsum has been the industry's standard dummy text .</p>
  <div class="byline">John Doe &nbsp;|&nbsp; <small>Orem Ipsum is simply</small></div>
</div>
<div class="avatar" role="img" aria-label="Customer portrait"></div>
<a class="arrow prev" href="#" aria-label="Previous">&#8249;</a>
<a class="arrow next" href="#" aria-label="Next">&#8250;</a>

<section class="blog">
  <h2 class="section-title" style="top:54px">OUR BLOG</h2>
  <article class="post" style="left:86px">
    <div class="post-photo" role="img" aria-label="Buffer polishing a car headlight"></div>
    <div class="post-meta">&#128197; 24 May 2017 &nbsp; &#128172; 0</div>
    <p>Lorem Ipsum is simply dummy text of the printing and typesetting industry. Lorem Ipsum has been the industry's standard dummy text ever since the 1500s, when an unknown printer took a galley of type and scrambled it to make a type specimen book .</p>
    <a class="more" href="#">READ MORE ...</a>
  </article>
  <article class="post" style="left:613px">
    <div class="post-photo" role="img" aria-label="Buffer polishing a car headlight"></div>
    <div class="post-meta">&#128197; 24 May 2017 &nbsp; &#128172; 0</div>
    <p>Lorem Ipsum is simply dummy text of the printing and typesetting industry. Lorem Ipsum has been the industry's standard dummy text ever since the 1500s, when an unknown printer took a galley of type and scrambled it to make a type specimen book .</p>
    <a class="more" href="#">READ MORE ...</a>
  </article>
  <a class="btn" href="#">View More</a>
</section>

<footer class="site-footer">
  <h4 style="left:86px">CONTACT US</h4>
  <div class="field" style="top:68px;height:33px">Name</div>
  <div class="field" style="top:113px;height:33px">Email</div>
  <div class="field" style="top:158px;height:119px">Message</div>
  <a class="btn" href="#">Send Message</a>

  <h4 style="left:612px">QUICK LINKS</h4>
  <ul class="quick">
    <li>Home</li><li>Car and Truck Detailing</li><li>Boat Detailing</li><li>Airplane Detailing</li><li>About Us</li><li>Contact Us</li>
  </ul>

  <h4 style="left:860px">CONTACTS</h4>
  <ul class="contacts">
    <li>Address: <span class="lower">Lorem Ipsum</span></li>
    <li>Phones: 000 - 0000 - 0000 , 000 - 0000 - 0000</li>
    <li>Hours: <span class="lower">7 days a week from 9:00 am to 7:00 pm</span></li>
    <li>E-mail: <span class="lower">info@keystonedetail.example</span></li>
  </ul>
</footer>

<div class="bottom-bar">
  <div class="social">
    <a href="#" aria-label="Social profile 1"></a><a href="#" aria-label="Social profile 2"></a><a href="#" aria-label="Social profile 3"></a><a href="#" aria-label="Social profile 4"></a>
  </div>
  <div class="copyright">© 2018 Keystone Mobile Detailing. All Right Reserved.</div>
</div>

</body>
</html>
```